Quorvel Equity _ Investment Manager

To design a professional flyer for a wealth management company

Investment Overview
• Quorvel Equity is a Fund Manager who specializes in Australian Property Investments.
• The Quorvel Equity Property Investment Fund’s attempt to invest in developments that encourages a 20-45% return during its term.
• We are attempting to take advantage of the current Australian property boom.
• Investors will invest directly into one direct property per application.
• We appoint a Trustee who will register each managed property investment with Australia’s regulators, the Federal Markets and Lending Authority (FMLA) http://www.fmlaoversight.net/mis

Investment Strategy
• Quorvel Equity will issue documentation (Information Memorandum or Product Disclosure Statement) per investment opportunity.
• Quorvel has built strong alliances with industry experts and property managers to support property asset selection.

About Quorvel Equity

Quorvel Equity is a wholly Australian owned funds manager, focused on investing in non-geared direct property by raising 100% of capital. We do not utilise borrowings from any financial institutions.

Our Strategic Partners

Quorvel Equity management team has a broad network of local partners with expertise in property management and funds management.
Fund Structure
Fund Quorvel Equity Property Fund

Fund Manager Quorvel Equity Pty Ltd
Targeted Offer Size $5,000,000+
Offer Type Wholesale and Retail

Fund Requirements 20%+ pa over term of holding
Minimum Application Investment Amount
$100,000 per investor
Investment project size $5mil - $35mil
Maximum Application Investment Amount Fund will not have a maximum investment offer amount.
Investment Term Minimum 1 Year
Investment Strategy The fund will invest in non-geared direct property Development across Australia.

The fund will abide by strict selection criteria and will be supported by local investment partners.

Target Market(s)

Property investors.
Superannuation investors (SMSF)

Industry/Entity Type

Investment

Requirements
Must have
• Design needs to cover double sided tri-fold
• Professional feel.
• Secured Investment
• Reflect Trust company
• Years of experience
Nice to have
• Innovative look and feel
Should not have
• Avoid tacky photos of investment (such as dollars signs, people standing around happy)
• Anything that makes us look desperate

```html
<!DOCTYPE html>
<html lang="en">
<head>
<meta charset="utf-8">
<title>Quorvel Equity – Tri-fold Brochure</title>
<link rel="stylesheet" href="https://fonts.googleapis.com/css2?family=Montserrat:wght@700&family=Open+Sans:wght@400;600&family=Cinzel:wght@400;600&display=swap">
<style>
  :root {
    --canvas: #e9eaec;
    --paper: #ffffff;
    --ink: #4a4f57;
    --blue-deep: #0d3f7e;
    --blue: #1a63b3;
    --blue-bright: #1e9be0;
    --blue-light: #6cc6f1;
    --sky: #9fd0f2;
    --rule: #1a5ea8;
  }
  * { box-sizing: border-box; margin: 0; padding: 0; }
  html, body { width: 1200px; height: 600px; overflow: hidden; }
  body {
    background: var(--canvas);
    font-family: "Open Sans", Arial, sans-serif;
    color: var(--ink);
    position: relative;
  }

  .inside-spread {
    position: absolute; left: 110px; top: 40px;
    width: 690px; height: 520px;
    display: flex;
    background: var(--paper);
    box-shadow: 0 6px 18px rgba(0,0,0,.18);
  }
  .panel { position: relative; width: 230px; height: 100%; overflow: hidden; }
  .panel + .panel { border-left: 1px solid #eceef1; }

  .photo { position: absolute; left: 0; width: 100%; }
  .photo--keys-house {
    top: 0; height: 250px;
    background: linear-gradient(150deg, var(--blue) 0%, var(--sky) 45%, #d9c7a6 100%);
    clip-path: polygon(0 0, 100% 0, 100% 62%, 0 100%);
  }
  .photo--meadow {
    top: 0; height: 175px;
    background: linear-gradient(180deg, #8cc7ee 0%, #cfe6f6 45%, #e8d66a 70%, #6aa63a 100%);
    clip-path: polygon(0 0, 100% 0, 100% 100%, 0 78%);
  }
  .photo--site-plan {
    top: 300px; left: 22px; width: 186px; height: 120px;
    background: linear-gradient(135deg, #eef0f2, #d7dbe0);
  }

  .panel-copy { position: absolute; left: 22px; right: 22px; }
  .section-heading {
    font-family: "Montserrat", Arial, sans-serif;
    font-weight: 700; font-size: 12px; letter-spacing: .3px;
    color: var(--blue); text-transform: uppercase;
    margin-bottom: 10px;
  }
  .body-text { font-size: 7.5px; line-height: 1.55; margin-bottom: 8px; }
  .bullets { list-style: none; }
  .bullets li { font-size: 7.5px; line-height: 1.55; margin-bottom: 6px; padding-left: 9px; position: relative; }
  .bullets li::before { content: ""; position: absolute; left: 0; top: 4px; width: 4px; height: 4px; background: var(--blue-bright); }
  .panel-rule { position: absolute; left: 22px; right: 22px; bottom: 34px; height: 3px; background: var(--rule); }

  .front-cover {
    position: absolute; left: 860px; top: 40px;
    width: 230px; height: 520px;
    background: var(--paper);
    overflow: hidden;
    box-shadow: 0 6px 18px rgba(0,0,0,.18);
  }
  .facets { position: absolute; left: 0; width: 100%; }
  .facets--top {
    top: 0; height: 120px;
    background: linear-gradient(135deg, var(--blue-light), var(--blue-bright) 45%, var(--blue) 100%);
    clip-path: polygon(0 0, 100% 0, 100% 45%, 0 100%);
  }
  .photo--hand-keys {
    top: 70px; height: 280px;
    background: linear-gradient(160deg, var(--blue) 0%, var(--sky) 35%, #e6cfb3 60%, #c9a878 100%);
  }
  .facets--bottom {
    top: 290px; height: 230px;
    background: linear-gradient(160deg, var(--blue-light) 0%, var(--blue-bright) 40%, var(--blue) 75%, var(--blue-deep) 100%);
    clip-path: polygon(0 28%, 100% 0, 100% 100%, 0 100%);
  }
  .cover-title {
    position: absolute; left: 38px; top: 368px; width: 154px;
    padding: 10px 8px 12px;
    background: rgba(255,255,255,.28);
    text-align: center;
  }
  .brand-name {
    display: inline-block;
    font-family: "Cinzel", Georgia, serif; font-weight: 600;
    font-size: 11px; letter-spacing: 1px; color: #ffffff;
    padding-bottom: 6px; margin-bottom: 6px;
    border-bottom: 1px solid rgba(255,255,255,.7);
  }
  .tagline {
    font-family: "Cinzel", Georgia, serif; font-weight: 400;
    font-size: 22px; line-height: 1.1; color: var(--blue-deep);
  }
  .cover-contact {
    position: absolute; left: 0; right: 0; bottom: 14px;
    text-align: center; color: #ffffff; font-size: 7px; line-height: 1.6;
  }
</style>
</head>
<body>

<section class="inside-spread" aria-label="Brochure inside spread">
  <article class="panel panel--partners">
    <div class="photo photo--keys-house" role="img" aria-label="Photo of a hand holding house keys beside a small model house"></div>
    <div class="panel-copy" style="top:285px">
      <h2 class="section-heading">Our Strategic Partners</h2>
      <p class="body-text">Quorvel Equity management team has a broad network of local partners with expertise in property management and funds management.</p>
      <p class="body-text">Quorvel has built strong alliances with industry experts and property managers to support property asset selection.</p>
      <p class="body-text">Together we assess each site, its market and its builder before any capital is committed.</p>
    </div>
    <div class="panel-rule"></div>
  </article>

  <article class="panel panel--overview">
    <div class="photo photo--meadow" role="img" aria-label="Photo of people relaxing in a sunny meadow of yellow flowers"></div>
    <div class="panel-copy" style="top:185px">
      <h2 class="section-heading">Investment Overview</h2>
      <ul class="bullets">
        <li>Quorvel Equity is a Fund Manager who specializes in Australian Property Investments.</li>
        <li>The Quorvel Equity Property Investment Fund’s attempt to invest in developments that encourages a 20-45% return during its term.</li>
        <li>We are attempting to take advantage of the current Australian property boom.</li>
        <li>Investors will invest directly into one direct property per application.</li>
        <li>We appoint a Trustee who will register each managed property investment with Australia’s regulators, the Federal Markets and Lending Authority (FMLA) http://www.fmlaoversight.net/mis</li>
      </ul>
    </div>
  </article>

  <article class="panel panel--about">
    <div class="panel-copy" style="top:40px">
      <h2 class="section-heading">About Us</h2>
      <p class="body-text">Quorvel Equity is a wholly Australian owned funds manager, focused on investing in non-geared direct property by raising 100% of capital.</p>
      <p class="body-text">We do not utilise borrowings from any financial institutions.</p>
      <p class="body-text">The fund will abide by strict selection criteria and will be supported by local investment partners.</p>
    </div>
    <div class="photo photo--site-plan" role="img" aria-label="Light grey site plan of a property development"></div>
    <div class="panel-rule"></div>
  </article>
</section>

<section class="front-cover" aria-label="Brochure front cover">
  <div class="photo photo--hand-keys" role="img" aria-label="Photo of a hand holding a key in front of a new home"></div>
  <div class="facets facets--top" role="img" aria-label="Faceted blue geometric shapes"></div>
  <div class="facets facets--bottom" role="img" aria-label="Faceted blue geometric shapes"></div>
  <div class="cover-title">
    <span class="brand-name">Quorvel Equity</span>
    <h1 class="tagline">We Can<br>Help</h1>
  </div>
  <p class="cover-contact">info@quorvelequity.net<br>Level 7, 18 Harbour Street, Brisbane</p>
</section>

</body>
</html>
```